Covid 19 Exit Strategy one page brochure

I would like to design, and will need URGENT help, a brochure detailing a Covid 19 Exit Strategy plan. This brochure will need to be understood easily and the graphics inside should make it easy for people to understand without reading the entire text. This project is quite urgent and needs to be completed THIS WEEK - by Saturday may 16th at the latest. I am attaching two examples. I will provide the text.

```html
<!DOCTYPE html>
<html lang="en">
<head>
<meta charset="utf-8">
<title>Exit Strategy Plan</title>
<link href="https://fonts.googleapis.com/css2?family=Anton&family=Rubik:wght@700&family=Montserrat:wght@500&display=swap" rel="stylesheet">
<style>
:root{
  --backdrop:#6b6c70;
  --paper:#ffffff;
  --paper-tint:#f4f5f7;
  --coral:#ef5257;
  --crimson:#d42c40;
  --text-red:#d0283f;
  --charcoal:#4a4e51;
  --white:#ffffff;
}
*{margin:0;padding:0;box-sizing:border-box}
html,body{width:1200px;height:2646px;overflow:hidden;background:var(--backdrop)}
.brochure{position:absolute;left:184px;top:184px;width:832px;height:2277px;background:var(--paper);box-shadow:10px 12px 18px rgba(0,0,0,.35);overflow:hidden}
.masthead{position:absolute;left:0;top:0;width:832px;height:455px;background:var(--paper-tint)}
.title{position:absolute;left:0;top:79px;width:832px;text-align:center;font-family:"Anton",sans-serif;font-weight:400;color:var(--coral);font-size:140px;line-height:150px;letter-spacing:-3px;white-space:nowrap}
.dark-band{position:absolute;left:0;top:1159px;width:832px;height:558px;background:var(--charcoal)}
.banner{position:absolute;left:61px;width:710px;height:95px}
.banner svg{position:absolute;left:0;top:0}
.banner-title{position:absolute;left:0;top:6px;width:710px;text-align:center;font-family:"Rubik",sans-serif;font-weight:700;color:var(--white);font-size:45px;line-height:52px}
.banner-sub{position:absolute;left:0;top:57px;width:710px;text-align:center;font-family:"Rubik",sans-serif;font-weight:700;color:var(--white);font-size:23px;line-height:26px}
.item{position:absolute;height:110px}
.item p{font-family:"Montserrat",sans-serif;font-weight:500;font-size:20.5px;line-height:27.5px;letter-spacing:.2px}
.item.left p{color:var(--text-red)}
.item.left{left:87px;width:720px}
.item.left .icon{position:absolute;left:0;top:-20px;width:113px;height:113px;color:var(--text-red)}
.item.left p{position:absolute;left:163px;top:0;white-space:nowrap}
.item.right{left:0;width:832px}
.item.right p{position:absolute;right:245px;top:0;text-align:right;white-space:nowrap;color:var(--white)}
.item.right .icon{position:absolute;left:638px;top:-14px;width:108px;height:108px;color:var(--white)}
.icon{fill:none;stroke:currentColor;stroke-width:3.2;stroke-linejoin:round;stroke-linecap:round}
</style>
</head>
<body>
<svg width="0" height="0" style="position:absolute" aria-hidden="true">
  <defs>
    <symbol id="ico-store" viewBox="0 0 100 100">
      <path d="M10 28 L18 8 H82 L90 28"/>
      <path d="M10 28 q5 8 10 0 q5 8 10 0 q5 8 10 0 q5 8 10 0 q5 8 10 0 q5 8 10 0 q5 8 10 0 q5 8 10 0"/>
      <path d="M26 8 L22 28 M38 8 L36 28 M50 8 V28 M62 8 L64 28 M74 8 L78 28"/>
      <path d="M14 34 V96 H86 V34"/>
      <path d="M22 96 V50 H42 V96 M22 70 H42"/>
      <rect x="52" y="50" width="24" height="20"/><path d="M50 76 H80 M66 84 H76"/>
    </symbol>
    <symbol id="ico-tower" viewBox="0 0 100 100">
      <rect x="26" y="6" width="56" height="90"/>
      <path d="M8 26 H26 V96 H8 Z M82 40 H94 V96 H82"/>
      <path d="M13 34 H20 M13 44 H20 M13 54 H20 M13 64 H20 M13 74 H20 M13 84 H20"/>
      <path d="M34 14 h8 v8 h-8z M48 14 h8 v8 h-8z M62 14 h8 v8 h-8z M34 30 h8 v8 h-8z M48 30 h8 v8 h-8z M62 30 h8 v8 h-8z M34 46 h8 v8 h-8z M48 46 h8 v8 h-8z M62 46 h8 v8 h-8z M34 62 h8 v8 h-8z M48 62 h8 v8 h-8z M62 62 h8 v8 h-8z"/>
      <path d="M44 96 V80 H64 V96 M54 80 V96 M86 50 h4 v6 h-4z M86 66 h4 v6 h-4z"/>
    </symbol>
    <symbol id="ico-patio" viewBox="0 0 100 100">
      <path d="M12 36 Q12 6 50 6 Q88 6 88 36 q-6 -6 -12.6 0 q-6 -6 -12.6 0 q-6 -6 -12.8 0 q-6 -6 -12.6 0 q-6 -6 -12.6 0 q-6 -6 -12.6 0z"/>
      <path d="M50 6 V70 M50 6 Q34 14 30 36 M50 6 Q66 14 70 36"/>
      <path d="M28 66 H72 M34 66 L66 96 M66 66 L34 96"/>
      <path d="M6 56 V96 M6 80 H22 V96 M94 56 V96 M94 80 H78 V96"/>
    </symbol>
    <symbol id="ico-chapel" viewBox="0 0 100 100">
      <path d="M50 4 V18 M44 10 H56"/>
      <path d="M24 44 L50 18 L76 44 M28 40 V96 M72 40 V96"/>
      <circle cx="50" cy="44" r="6"/>
      <path d="M28 58 L8 72 V96 H92 V72 L72 58 M14 96 V76 M86 96 V76"/>
      <path d="M42 96 V76 Q50 66 58 76 V96"/>
      <rect x="33" y="72" width="5" height="10" rx="2.5"/><rect x="62" y="72" width="5" height="10" rx="2.5"/>
    </symbol>
    <symbol id="ico-table" viewBox="0 0 100 100">
      <path d="M26 38 H74 M50 38 V52 M34 52 L66 88 M66 52 L34 88 M40 52 H60"/>
      <path d="M4 30 V88 M4 60 H20 V88 M96 30 V88 M96 60 H80 V88"/>
      <path d="M40 38 V30 M60 38 V30"/>
    </symbol>
    <symbol id="ico-stage" viewBox="0 0 100 100">
      <rect x="4" y="6" width="92" height="88"/>
      <path d="M4 18 H96"/>
      <path d="M10 18 q5 8 10 0 q5 8 10 0 M70 18 q5 8 10 0 q5 8 10 0 M36 18 q7 6 14 0 q7 6 14 0"/>
      <path d="M4 28 Q26 50 24 94 M96 28 Q74 50 76 94"/>
      <path d="M10 94 Q10 80 22 74 M90 94 Q90 80 78 74"/>
    </symbol>
    <symbol id="ico-calendar" viewBox="0 0 100 100">
      <rect x="4" y="12" width="92" height="84" rx="4"/>
      <path d="M4 30 H96 M22 4 V20 M40 4 V20 M60 4 V20 M78 4 V20"/>
      <path d="M50 42 L53.5 50 L62 50.5 L55.5 56 L57.5 64 L50 59.5 L42.5 64 L44.5 56 L38 50.5 L46.5 50 Z"/>
      <path d="M16 52 h6 v6 h-6z M28 52 h6 v6 h-6z M66 52 h6 v6 h-6z M78 52 h6 v6 h-6z M16 72 h6 v6 h-6z M28 72 h6 v6 h-6z M40 72 h6 v6 h-6z M54 72 h6 v6 h-6z M66 72 h6 v6 h-6z M78 72 h6 v6 h-6z"/>
    </symbol>
  </defs>
</svg>

<main class="brochure">
  <div class="masthead"></div>
  <h1 class="title">EXIT STRATEGY<br>PLAN</h1>
  <div class="dark-band"></div>

  <section class="banner" style="top:414px">
    <svg width="710" height="95" viewBox="0 0 710 95" aria-hidden="true">
      <rect x="0" y="0" width="710" height="41" fill="var(--charcoal)"/>
      <path d="M0 0 H710 L618 80 Q355 94 92 80 Z" fill="var(--coral)"/>
    </svg>
    <h2 class="banner-title">Your Text Here</h2>
    <p class="banner-sub">Lorem ipsum dolor</p>
  </section>

  <div class="item left" style="top:564px"><svg class="icon"><use href="#ico-store"/></svg><p>Lorem ipsum dolor sit amet, consectetuer<br>adipiscing elit, sed diam nonummy nibh<br>euismod tincidunt ut laoreet dolore</p></div>
  <div class="item left" style="top:697px"><svg class="icon"><use href="#ico-tower"/></svg><p>Lorem ipsum dolor sit amet, consectetuer<br>adipiscing elit, sed diam nonummy nibh<br>euismod tincidunt ut laoreet dolore</p></div>
  <div class="item left" style="top:825px"><svg class="icon"><use href="#ico-patio"/></svg><p>Lorem ipsum dolor sit amet, consectetuer<br>adipiscing elit, sed diam nonummy nibh<br>euismod tincidunt ut laoreet dolore</p></div>
  <div class="item left" style="top:972px"><svg class="icon" style="top:-34px;height:126px"><use href="#ico-chapel"/></svg><p>Lorem ipsum dolor sit amet, consectetuer<br>adipiscing elit, sed diam nonummy nibh<br>euismod tincidunt ut laoreet dolore</p></div>

  <section class="banner" style="top:1115px">
    <svg width="710" height="95" viewBox="0 0 710 95" aria-hidden="true">
      <rect x="0" y="0" width="710" height="41" fill="var(--coral)"/>
      <path d="M0 0 H710 L618 80 Q355 94 92 80 Z" fill="var(--crimson)"/>
    </svg>
    <h2 class="banner-title">Your Text Here</h2>
    <p class="banner-sub">Lorem ipsum dolor</p>
  </section>

  <div class="item right" style="top:1257px"><p>Lorem ipsum dolor sit amet, consectetuer<br>adipiscing elit, sed diam nonummy nibh<br>euismod tincidunt ut laoreet dolore</p><svg class="icon" style="top:-16px;height:80px"><use href="#ico-table"/></svg></div>
  <div class="item right" style="top:1389px"><p>Lorem ipsum dolor sit amet, consectetuer<br>adipiscing elit, sed diam nonummy nibh<br>euismod tincidunt ut laoreet dolore</p><svg class="icon" style="top:-16px;height:100px"><use href="#ico-stage"/></svg></div>
  <div class="item right" style="top:1538px"><p>Lorem ipsum dolor sit amet, consectetuer<br>adipiscing elit, sed diam nonummy nibh<br>euismod tincidunt ut laoreet dolore</p><svg class="icon" style="top:-22px;height:104px"><use href="#ico-calendar"/></svg></div>

  <section class="banner" style="top:1675px">
    <svg width="710" height="95" viewBox="0 0 710 95" aria-hidden="true">
      <rect x="0" y="0" width="710" height="41" fill="var(--crimson)"/>
      <path d="M0 0 H710 L618 80 Q355 94 92 80 Z" fill="var(--coral)"/>
    </svg>
    <h2 class="banner-title">Your Text Here</h2>
    <p class="banner-sub">Lorem ipsum dolor</p>
  </section>

  <div class="item left" style="top:1830px"><svg class="icon"><use href="#ico-store"/></svg><p>Lorem ipsum dolor sit amet, consectetuer<br>adipiscing elit, sed diam nonummy nibh<br>euismod tincidunt ut laoreet dolore</p></div>
  <div class="item left" style="top:1963px"><svg class="icon"><use href="#ico-tower"/></svg><p>Lorem ipsum dolor sit amet, consectetuer<br>adipiscing elit, sed diam nonummy nibh<br>euismod tincidunt ut laoreet dolore</p></div>
  <div class="item left" style="top:2092px"><svg class="icon"><use href="#ico-patio"/></svg><p>Lorem ipsum dolor sit amet, consectetuer<br>adipiscing elit, sed diam nonummy nibh<br>euismod tincidunt ut laoreet dolore</p></div>
</main>
</body>
</html>
```